YARD FRONTS "N" MORE

catyering to driveway/patio floor construction and remodeling. Concrete, concrete pavers, asphalt, Landscaping, irrigation, pergolas and pools.

Target Market(s)

the home owner that wants to enhance their home

Industry/Entity Type

construction

Contact Information for Business Card

presidet: tomas bellweather email: yardfrontsnmore@example.come office/cell: 555 214 8830

Font styles to use
Sans Serif

Requirements
Must have
• logo should pop out
Nice to have
• the logo should demonstrate that we do exteriors only

```html
<!DOCTYPE html>
<html lang="en">
<head>
<meta charset="utf-8">
<title>Yard Fronts "N" More — Business Card</title>
<link href="https://fonts.googleapis.com/css2?family=Anton&family=Roboto:wght@400&display=swap" rel="stylesheet">
<style>
  :root {
    --slate: #45434d;
    --white: #ffffff;
    --ink: #111111;
    --brand-blue: #0a88c8;
    --page: #ffffff;
  }
  * { margin: 0; padding: 0; box-sizing: border-box; }
  html, body { width: 1200px; height: 1000px; overflow: hidden; background: var(--page); }
  .canvas { position: relative; width: 1200px; height: 1000px; }

  .card { position: absolute; left: 316px; width: 567px; height: 325px; overflow: hidden; }
  .card-front { top: 130px; background: var(--slate); }
  .card-back { top: 528px; background: var(--white); box-shadow: 0 0 10px rgba(0,0,0,0.25); }

  .wordmark { position: absolute; font-family: "Anton", "Oswald", sans-serif; font-weight: 400; text-transform: uppercase; text-align: center; line-height: 1; }
  .card-front .wordmark { left: 0; right: 0; top: 86px; color: var(--white); }
  .card-front .wordmark .line-top { display: block; font-size: 42px; letter-spacing: 0.5px; }
  .card-front .wordmark .line-bottom { display: block; font-size: 72px; margin-top: 6px; letter-spacing: 1px; }

  .card-back .wordmark { left: 26px; top: 22px; width: 180px; color: var(--brand-blue); }
  .card-back .wordmark .line-top { display: block; font-size: 28px; }
  .card-back .wordmark .line-bottom { display: block; font-size: 48px; margin-top: 3px; }

  .accent-shape { position: absolute; left: 0; top: 0; }

  .person { position: absolute; left: 104px; width: 360px; top: 118px; text-align: center; }
  .person-name { font-family: "Anton", "Oswald", sans-serif; font-size: 40px; color: var(--slate); line-height: 1.1; white-space: nowrap; }
  .person-title { font-family: "Roboto", Arial, sans-serif; font-size: 21px; color: var(--ink); margin-top: 2px; letter-spacing: 0.3px; }

  .contact { position: absolute; left: 134px; top: 226px; list-style: none; font-family: "Roboto", Arial, sans-serif; font-size: 19px; color: var(--ink); }
  .contact li { display: flex; align-items: center; height: 30px; white-space: nowrap; }
  .contact svg { width: 16px; height: 18px; margin-right: 6px; flex: none; }
</style>
</head>
<body>
<main class="canvas">
  <section class="card card-front" aria-label="Card front">
    <h1 class="wordmark"><span class="line-top">Yard Fronts</span><span class="line-bottom">"N" More</span></h1>
  </section>

  <section class="card card-back" aria-label="Card back">
    <svg class="accent-shape" width="567" height="325" viewBox="0 0 567 325" aria-hidden="true">
      <polygon points="509,0 567,0 567,22 507,19" fill="var(--slate)"/>
      <polygon points="498,35 567,35 567,293 449,297" fill="var(--slate)"/>
      <polygon points="448,306 567,303 567,325 444,325" fill="var(--slate)"/>
    </svg>

    <div class="wordmark"><span class="line-top">Yard Fronts</span><span class="line-bottom">"N" More</span></div>

    <div class="person">
      <p class="person-name">Tomas Bellweather</p>
      <p class="person-title">PRESIDET</p>
    </div>

    <ul class="contact">
      <li>
        <svg viewBox="0 0 16 18" aria-hidden="true"><rect x="0" y="4" width="16" height="11" fill="var(--brand-blue)"/><polyline points="0,4 8,10 16,4" fill="none" stroke="#fff" stroke-width="1.5"/></svg>
        yardfrontsnmore@example.come
      </li>
      <li>
        <svg viewBox="0 0 16 18" aria-hidden="true"><rect x="2.5" y="1" width="11" height="16" rx="2" fill="none" stroke="var(--brand-blue)" stroke-width="2"/><circle cx="8" cy="14" r="1" fill="var(--brand-blue)"/></svg>
        555 214 8830
      </li>
    </ul>
  </section>
</main>
</body>
</html>
```